Kettle Lane Kitchen February contest

The website slider is 990 X 225 pixels to fit in with this website www.kettlelanekitchen.com.au
We would love a fun, lively, food-oriented slider created for Kettle Lane Kitchen website. Kettle Lane Kitchen is a central place where people who love food, cooking for their family and friends, and sharing recipes can hang out. We'd like the sliders to be simple, bright and to entice people to click on the link.
The banner ad needs to feature the Varnholt mixer, and to use a colour scheme that also works with the existing website. There's a blog with more information on the Varnholt mixer here http://kettlelanekitchen.com.au/uncategorized/upload-a-recipe-in-february-to-be-in-the-running-to-win-a-varnholt-mixer/
A slider in December was used to promote a similar competition which I will upload as inspiration, along with the image of the Varnholt mixer to use.
Main text: Add your best recipe by February 28 to win!
Smaller text: Best recipe as chosen by Kettle Lane Kitchen editors will win a Varnholt mixer worth $699.
Target Market(s)
Food lovers - home cooks and food bloggers. Mainly women, 30+
Industry/Entity Type
Chef

```html
<!DOCTYPE html>
<html lang="en">
<head>
<meta charset="utf-8">
<title>Kettle Lane Kitchen – February contest</title>
<link href="https://fonts.googleapis.com/css2?family=Didact+Gothic&family=Archivo:ital,wght@0,400;0,700;0,800;1,900&family=Arimo:wght@400;700&display=swap" rel="stylesheet">
<style>
  :root {
    --paper: #efe5d8;
    --paper-light: #f5eee5;
    --ink: #4a3a30;
    --orange: #dd5025;
    --orange-deep: #cf4519;
    --grey-text: #4d4a48;
    --white: #ffffff;
    --photo-cream: #e7dccf;
    --photo-red: #c2472d;
    --photo-green: #7c9a3c;
    --mixer-teal: #35b6c9;
    --mixer-steel: #c9ccce;
  }
  * { box-sizing: border-box; margin: 0; padding: 0; }
  html, body { width: 1200px; height: 415px; overflow: hidden; }
  body {
    background: radial-gradient(ellipse at 40% 30%, var(--paper-light), var(--paper) 70%);
    font-family: "Arimo", Arial, sans-serif;
  }
  .stage {
    position: relative;
    width: 1110px;
    height: 384px;
    transform: scale(1.081);
    transform-origin: 0 0;
  }

  /* Brand */
  .brand {
    position: absolute;
    left: 53px; top: -22px;
    width: 178px; height: 178px;
    border-radius: 50%;
    background: var(--white);
    display: flex; align-items: center; justify-content: center;
    z-index: 3;
  }
  .brand-ring {
    position: absolute; inset: 9px;
    border-radius: 50%;
    border: 3px solid var(--ink);
  }
  .brand-name {
    font-family: "Didact Gothic", sans-serif;
    color: var(--ink);
    font-size: 25px;
    line-height: 1.05;
    text-align: center;
    margin-top: 20px;
  }

  /* Account */
  .account {
    position: absolute;
    left: 925px; top: 0;
    width: 118px; height: 28px;
    background: var(--white);
    border-radius: 0 0 6px 6px;
    display: flex; justify-content: center; align-items: center; gap: 14px;
    font-size: 12.5px;
  }
  .account a { color: var(--orange); text-decoration: none; }

  .tagline {
    position: absolute;
    left: 392px; top: 33px;
    font-family: "Didact Gothic", sans-serif;
    font-size: 29px;
    letter-spacing: 0.5px;
    color: var(--ink);
  }
  .tagline-arrow { position: absolute; left: 798px; top: 38px; }

  /* Navigation */
  .nav-community {
    position: absolute;
    left: 238px; top: 100px;
    width: 305px; height: 40px;
    background: var(--white);
    display: flex; align-items: center; gap: 22px;
    padding-left: 24px;
    font-size: 12.5px; font-weight: 700; color: #2d2a28;
  }
  .nav-community span { display: flex; align-items: center; gap: 5px; }
  .nav-site {
    position: absolute;
    left: 543px; top: 100px;
    width: 500px; height: 40px;
    background: var(--orange);
    border-radius: 0 5px 0 0;
    display: flex; align-items: center; justify-content: center; gap: 9px;
    font-size: 12.5px; font-weight: 700; color: var(--white);
  }
  .nav-site .dot { width: 4px; height: 4px; border-radius: 50%; background: var(--white); }

  /* Slider */
  .slider {
    position: absolute;
    left: 53px; top: 144px;
    width: 990px; height: 225px;
    background: linear-gradient(90deg, #f1e7de 0%, #fbf8f5 40%, #f7f1ec 62%);
    overflow: hidden;
  }
  .slider-photo { position: absolute; left: 0; top: 0; }
  .mixer {
    position: absolute;
    left: 88px; top: 28px;
    width: 205px; height: 160px;
  }
  .headline {
    position: absolute;
    left: 317px; top: 34px;
    width: 240px;
    text-align: center;
    font-family: "Archivo", sans-serif;
    color: var(--grey-text);
  }
  .headline .line { font-size: 25px; font-weight: 400; line-height: 31px; letter-spacing: 0.3px; }
  .headline .accent { font-size: 27px; font-weight: 800; color: var(--orange); letter-spacing: 1px; line-height: 30px; }
  .headline .win {
    font-size: 47px; font-weight: 900; font-style: italic;
    color: var(--orange-deep); line-height: 56px; letter-spacing: 1px;
    margin-left: -10px;
  }
  .pointer { position: absolute; left: 282px; top: 122px; }
  .fineprint {
    position: absolute;
    left: 75px; top: 198px;
    font-size: 12.5px; color: var(--grey-text);
  }
  .fineprint strong { font-size: 15px; font-weight: 700; }

  .content-top {
    position: absolute;
    left: 53px; top: 369px;
    width: 990px; height: 15px;
    background: var(--white);
  }
</style>
</head>
<body>
<div class="stage">
  <div class="brand"><div class="brand-ring"></div><div class="brand-name">Kettle<br>Lane<br>Kitchen</div></div>

  <nav class="account"><a href="#">Register</a><a href="#">Login</a></nav>

  <p class="tagline">Join the community now!</p>
  <svg class="tagline-arrow" width="50" height="26" viewBox="0 0 50 26">
    <path d="M3 20 Q25 24 44 6" fill="none" stroke="var(--orange)" stroke-width="2" stroke-linecap="round"/>
    <path d="M36 5 L45 4 L44 13" fill="none" stroke="var(--orange)" stroke-width="2" stroke-linecap="round" stroke-linejoin="round"/>
  </svg>

  <nav class="nav-community">
    <span><svg width="20" height="14" viewBox="0 0 20 14"><path d="M1 5 H19 Q18 13 10 13 Q2 13 1 5Z" fill="var(--orange)"/><path d="M12 4 L17 0" stroke="var(--orange)" stroke-width="1.5"/></svg>Recipes</span>
    <span><svg width="18" height="16" viewBox="0 0 18 16"><circle cx="5" cy="6" r="4" fill="var(--orange)"/><circle cx="13" cy="6" r="4" fill="var(--orange)"/><circle cx="9" cy="4" r="4" fill="var(--orange)"/><rect x="4" y="8" width="10" height="7" fill="var(--orange)"/></svg>Chefs</span>
    <span><svg width="20" height="17" viewBox="0 0 20 17"><circle cx="4" cy="7" r="2.6" fill="var(--orange)"/><circle cx="8" cy="3" r="2.6" fill="var(--orange)"/><circle cx="13" cy="3" r="2.6" fill="var(--orange)"/><circle cx="17" cy="7" r="2.6" fill="var(--orange)"/><ellipse cx="10.5" cy="12" rx="5" ry="4" fill="var(--orange)"/></svg>Mentors</span>
  </nav>

  <nav class="nav-site">
    <span>Upload your recipe</span><i class="dot"></i><span>Prizes</span><i class="dot"></i><span>About</span><i class="dot"></i><span>FAQs</span><i class="dot"></i><span>Contact</span><i class="dot"></i><span>Blog</span>
  </nav>

  <section class="slider">
    <svg class="slider-photo" width="990" height="225" viewBox="0 0 990 225" role="img" aria-label="Photo of a hand sprinkling grated cheese over a plate of spaghetti with tomato sauce and basil">
      <defs>
        <linearGradient id="dish" x1="0" y1="0" x2="0.6" y2="1">
          <stop offset="0" stop-color="var(--photo-cream)"/>
          <stop offset="0.5" stop-color="#eadfd3"/>
          <stop offset="0.8" stop-color="#d79a6e"/>
          <stop offset="1" stop-color="var(--photo-red)"/>
        </linearGradient>
      </defs>
      <polygon points="637,0 990,0 990,225 567,225" fill="url(#dish)"/>
    </svg>

    <svg class="mixer" viewBox="0 0 205 160" role="img" aria-label="Varnholt stand mixer in turquoise with a steel bowl">
      <defs>
        <linearGradient id="mixerTone" x1="0" y1="0" x2="1" y2="1">
          <stop offset="0" stop-color="var(--mixer-steel)"/>
          <stop offset="0.55" stop-color="var(--mixer-teal)"/>
          <stop offset="1" stop-color="#9aa3a6"/>
        </linearGradient>
      </defs>
      <rect x="0" y="0" width="205" height="160" rx="18" fill="url(#mixerTone)" opacity="0.85"/>
    </svg>

    <svg class="pointer" width="46" height="30" viewBox="0 0 46 30">
      <path d="M2 4 Q24 2 40 22" fill="none" stroke="var(--orange)" stroke-width="1.8" stroke-linecap="round"/>
      <path d="M31 20 L41 24 L40 13" fill="none" stroke="var(--orange)" stroke-width="1.8" stroke-linecap="round" stroke-linejoin="round"/>
    </svg>

    <div class="headline">
      <p class="line">ADD YOUR</p>
      <p class="accent">BEST RECIPE</p>
      <p class="line">BY FEBRUARY 28</p>
      <p class="win">TO WIN</p>
    </div>

    <p class="fineprint">*Best recipe as chosen by Kettle Lane Kitchen editors will win a Varnholt mixer worth <strong>$699.</strong></p>
  </section>

  <div class="content-top"></div>
</div>
</body>
</html>
```